Creative Business Card

Were looking for a new fresh and creative look to our Business card. Our company name is InkVale. Be creative, Were attaching our logo and our base colors, but your free to do anything. Name, title, Phone

Industry/Entity Type

Business

```html
<!DOCTYPE html>
<html lang="en">
<head>
<meta charset="utf-8">
<title>InkVale Business Card</title>
<link href="https://fonts.googleapis.com/css2?family=Source+Sans+3:wght@400;600;700&display=swap" rel="stylesheet">
<style>
  :root {
    --page: #d4d4d6;
    --card-dark: #262626;
    --brand-blue: #0072bc;
    --light-blue: #4a9ddb;
    --brand-green: #72bf44;
    --text-light: #ffffff;
  }
  * { margin: 0; padding: 0; box-sizing: border-box; }
  html, body {
    width: 883px;
    height: 1200px;
    overflow: hidden;
    background: var(--page);
    font-family: "Source Sans 3", "Myriad Pro", Arial, sans-serif;
  }
  .presentation {
    position: relative;
    width: 883px;
    height: 1200px;
  }
  .card-slot {
    position: absolute;
    left: 141.5px;
    width: 600px;
    height: 335px;
  }
  .card-slot--front { top: 245px; }
  .card-slot--back { top: 620px; }
  .card {
    position: absolute;
    top: 0;
    left: 0;
    width: 390px;
    height: 218px;
    overflow: hidden;
    transform: scale(1.5385);
    transform-origin: 0 0;
    box-shadow: 0 2px 4px rgba(0,0,0,0.25);
  }
  .card__shapes {
    position: absolute;
    inset: 0;
    width: 390px;
    height: 218px;
    display: block;
  }
  .shape-dark { fill: var(--card-dark); }
  .shape-blue { fill: var(--brand-blue); }
  .shape-light { fill: var(--light-blue); }

  .brand-name {
    position: absolute;
    color: var(--brand-green);
    font-weight: 700;
    font-size: 29px;
    line-height: 1;
    letter-spacing: 0.5px;
    text-transform: uppercase;
  }
  .card--front .brand-name { left: 182px; top: 94px; }
  .card--back .brand-name { left: 24px; top: 17px; }

  .holder {
    position: absolute;
    left: 25px;
    top: 74px;
  }
  .holder__name {
    color: var(--brand-blue);
    font-weight: 700;
    font-size: 13.5px;
    line-height: 1.1;
  }
  .holder__title {
    color: var(--text-light);
    font-size: 10.5px;
    line-height: 1.2;
  }
  .contact-list {
    position: absolute;
    left: 25px;
    top: 134px;
    list-style: none;
  }
  .contact-list li {
    display: flex;
    align-items: center;
    height: 11.5px;
    color: var(--text-light);
    font-size: 10.5px;
  }
  .contact-icon {
    width: 9px;
    height: 9px;
    margin-right: 10px;
    flex: none;
    color: var(--brand-green);
    font-size: 8px;
    font-weight: 600;
    line-height: 9px;
  }
  .contact-icon svg { width: 9px; height: 9px; display: block; }
</style>
</head>
<body>
<main class="presentation">

  <section class="card-slot card-slot--front">
    <div class="card card--front">
      <svg class="card__shapes" viewBox="0 0 390 218" aria-hidden="true">
        <rect class="shape-blue" x="0" y="0" width="390" height="218"/>
        <polygon class="shape-dark" points="125,0 310,0 334,37 390,175 390,218 195,218"/>
        <polygon class="shape-light" points="310,0 390,0 334,37"/>
      </svg>
      <div class="brand-name">InkVale</div>
    </div>
  </section>

  <section class="card-slot card-slot--back">
    <div class="card card--back">
      <svg class="card__shapes" viewBox="0 0 390 218" aria-hidden="true">
        <rect class="shape-dark" x="0" y="0" width="390" height="218"/>
        <polygon class="shape-light" points="240,0 320,0 297,73"/>
        <polygon class="shape-blue" points="320,0 390,0 390,218 245,218 297,73"/>
      </svg>
      <div class="brand-name">InkVale</div>
      <div class="holder">
        <p class="holder__name">Your Name</p>
        <p class="holder__title">Your title</p>
      </div>
      <ul class="contact-list">
        <li>
          <span class="contact-icon"><svg viewBox="0 0 10 10"><path fill="currentColor" d="M1 3.5 Q5 0.5 9 3.5 L8 5 L6.5 4.3 L6.5 3.4 Q5 3 3.5 3.4 L3.5 4.3 L2 5 Z M2.5 6 H7.5 V9 H2.5 Z"/></svg></span>
          0123 456 789
        </li>
        <li>
          <span class="contact-icon"><svg viewBox="0 0 10 10"><rect x="2.5" y="0.8" width="5" height="8.4" rx="0.8" fill="none" stroke="currentColor" stroke-width="1"/></svg></span>
          0123 456 789
        </li>
        <li>
          <span class="contact-icon">Fx</span>
          0123 456 789
        </li>
        <li>
          <span class="contact-icon"><svg viewBox="0 0 10 10"><rect x="0.8" y="2" width="8.4" height="6" fill="currentColor"/><path d="M1 2.3 L5 5.5 L9 2.3" fill="none" stroke="#262626" stroke-width="0.8"/></svg></span>
          youremail@mail.com
        </li>
        <li>
          <span class="contact-icon"><svg viewBox="0 0 10 10"><circle cx="5" cy="5" r="4" fill="none" stroke="currentColor" stroke-width="0.9"/><ellipse cx="5" cy="5" rx="1.8" ry="4" fill="none" stroke="currentColor" stroke-width="0.7"/><path d="M1 5 H9" stroke="currentColor" stroke-width="0.7"/></svg></span>
          www.yourwebdite.com
        </li>
      </ul>
    </div>
  </section>

</main>
</body>
</html>
```